Commerical Office Furniture Company Needs Truck Wrap Design for Box Truck

We need a truck wrap design (and business card) for our company based in Fresno, California. We offer commercial office furnishings such as private office desks, cubicle stations, conference tables, all office seating (task chairs, guest, lobby/lounge, conference) storage systems, ergonomic solutions (monitor arms, keyboard trays, lift desks) and much more. We are a full service office furniture dealer who can fully outfit every space and need for a new or existing office space. We also offer design and space planning services and professional installation.
We would like our trap wrap to be modern using the same color scheme as our logo with a clean but eye catching look. Perhaps using a few nice looking desk/workstations product images as examples to show people what we are capable of. We attached some examples of some themes/layouts we like. feel free to be creative. Our website tembrolight.com has some images and info.
https://imagelibrary.brv-corp.com/detail/client-space-shared-prism-workstation-with-t-line-storage-height-adjustable-tables-and-dorval-seating
Target Market(s)
Private Sector, Education, Healthcare
Industry/Entity Type
Requirements
Must have
- Varto Box Truck - 190 inches x 85 inches

```html
<!DOCTYPE html>
<html lang="en">
<head>
<meta charset="utf-8">
<title>Tembrolight Office Interiors – Truck Wrap</title>
<link href="https://fonts.googleapis.com/css2?family=Open+Sans:wght@400;600;700&display=swap" rel="stylesheet">
<style>
  :root {
    --brand-blue: #1f6ff2;
    --charcoal: #4a4c50;
    --band: #f4f4f5;
    --page: #e9eaec;
    --photo-white: #f7f8f9;
    --photo-light: #e4e6e9;
    --photo-mid: #c3c7cc;
    --photo-dark: #8e9399;
    --screen-blue: #8393b0;
    --desk-wood: #d9d2c8;
    --panel-edge: #b9bcc0;
  }
  * { box-sizing: border-box; margin: 0; padding: 0; }
  html, body { width: 1028px; height: 1200px; overflow: hidden; }
  body {
    background: var(--page);
    font-family: "Open Sans", Arial, sans-serif;
    position: relative;
  }

  .wrap-panel {
    position: absolute;
    background: #fff;
    border: 1px solid var(--panel-edge);
    overflow: hidden;
  }
  .side-panel { left: 34px; top: 30px; width: 960px; height: 430px; }
  .cab-panel { left: 34px; top: 520px; width: 450px; height: 230px; border-radius: 18px 18px 6px 6px; }
  .rear-panel { left: 524px; top: 520px; width: 470px; height: 640px; }

  .contact-band {
    position: absolute; left: 0; right: 0; top: 0;
    background: var(--band);
    border-bottom: 1px solid #d8d9db;
    display: flex; justify-content: center; align-items: center;
    color: var(--brand-blue);
    font-weight: 600; letter-spacing: 0.12em;
    z-index: 2;
  }
  .side-panel .contact-band { height: 78px; font-size: 30px; gap: 40px; }
  .rear-panel .contact-band { height: 92px; font-size: 16px; gap: 22px; }

  .workspace-photo {
    position: absolute; left: 0; right: 0; bottom: 0;
  }
  .side-panel .workspace-photo {
    top: 78px;
    background:
      radial-gradient(ellipse 30% 62% at 50% 55%, rgba(255,255,255,0.96), rgba(255,255,255,0) 100%),
      radial-gradient(ellipse 9% 16% at 10% 36%, rgba(131,147,176,0.75), rgba(131,147,176,0) 100%),
      radial-gradient(ellipse 9% 16% at 90% 36%, rgba(131,147,176,0.75), rgba(131,147,176,0) 100%),
      linear-gradient(180deg, var(--photo-light) 0%, var(--photo-white) 28%, var(--photo-mid) 42%, var(--desk-wood) 58%, #d4d6d9 72%, var(--photo-dark) 100%);
  }
  .rear-panel .workspace-photo {
    top: 92px;
    background:
      radial-gradient(ellipse 45% 40% at 55% 52%, rgba(255,255,255,0.92), rgba(255,255,255,0) 100%),
      radial-gradient(ellipse 18% 20% at 85% 66%, rgba(131,147,176,0.6), rgba(131,147,176,0) 100%),
      linear-gradient(180deg, var(--photo-mid) 0%, var(--photo-white) 30%, var(--photo-light) 55%, var(--desk-wood) 68%, var(--photo-mid) 82%, var(--photo-dark) 100%);
  }

  .brand-lockup {
    position: absolute; left: 0; right: 0;
    text-align: center;
    z-index: 1;
  }
  .brand-square {
    display: block; margin: 0 auto;
    background: var(--brand-blue);
  }
  .brand-primary {
    color: var(--brand-blue);
    font-weight: 600;
    line-height: 1.05;
  }
  .brand-secondary {
    color: var(--charcoal);
    font-weight: 600;
    display: flex; justify-content: center; align-items: center;
  }
  .brand-secondary::before, .brand-secondary::after {
    content: ""; display: block; height: 2px; background: var(--charcoal);
  }
  .services { color: var(--charcoal); }
  .services span + span::before { content: "•"; margin: 0 0.9em; }
  .selling-points { color: var(--brand-blue); font-weight: 600; line-height: 1.45; }

  /* side */
  .side-panel .brand-lockup { top: 124px; }
  .side-panel .brand-square { width: 54px; height: 54px; margin-bottom: 24px; }
  .side-panel .brand-primary { font-size: 36px; }
  .side-panel .brand-secondary { font-size: 24px; letter-spacing: 0.45em; gap: 10px; margin-top: 2px; }
  .side-panel .brand-secondary::before, .side-panel .brand-secondary::after { width: 24px; }
  .side-panel .services { font-size: 16px; margin-top: 4px; }
  .side-panel .selling-points { font-size: 14px; margin-top: 6px; }

  /* cab */
  .cab-panel .brand-lockup { top: 42px; }
  .cab-panel .brand-square { width: 34px; height: 34px; margin-bottom: 16px; }
  .cab-panel .brand-primary { font-size: 22px; }
  .cab-panel .brand-secondary { font-size: 14px; letter-spacing: 0.45em; gap: 8px; }
  .cab-panel .brand-secondary::before, .cab-panel .brand-secondary::after { width: 16px; }
  .cab-panel .services { font-size: 10px; margin-top: 4px; }

  /* rear */
  .rear-panel .brand-lockup { top: 290px; }
  .rear-panel .brand-square { width: 66px; height: 66px; margin-bottom: 28px; }
  .rear-panel .brand-primary { font-size: 32px; }
  .rear-panel .brand-secondary { font-size: 22px; letter-spacing: 0.45em; gap: 10px; margin-top: 4px; }
  .rear-panel .brand-secondary::before, .rear-panel .brand-secondary::after { width: 22px; }
  .rear-panel .services { font-size: 15px; margin-top: 6px; }
</style>
</head>
<body>

  <section class="wrap-panel side-panel" aria-label="Side wrap">
    <div class="contact-band"><span>(555) 014-2270</span><span>WWW.TEMBROLIGHT.COM</span></div>
    <div class="workspace-photo" role="img" aria-label="Photo of a bright open office with shared workstations, blue privacy screens, height-adjustable desks and white task chairs"></div>
    <div class="brand-lockup">
      <span class="brand-square" aria-hidden="true"></span>
      <p class="brand-primary">TEMBROLIGHT OFFICE</p>
      <p class="brand-secondary">INTERIORS</p>
      <p class="services"><span>Office Furniture</span><span>Design</span><span>Installation</span></p>
      <p class="selling-points">• Family owned and operated for 25+ years<br>• Call to schedule free consultation</p>
    </div>
  </section>

  <section class="wrap-panel cab-panel" aria-label="Cab header">
    <div class="brand-lockup">
      <span class="brand-square" aria-hidden="true"></span>
      <p class="brand-primary">TEMBROLIGHT OFFICE</p>
      <p class="brand-secondary">INTERIORS</p>
      <p class="services"><span>Office Furniture</span><span>Design</span><span>Installation</span></p>
    </div>
  </section>

  <section class="wrap-panel rear-panel" aria-label="Rear doors">
    <div class="contact-band"><span>(555) 014-2270</span><span>WWW.TEMBROLIGHT.COM</span></div>
    <div class="workspace-photo" role="img" aria-label="Photo of a modern office interior with large windows, a workstation desk with blue screen and a white task chair"></div>
    <div class="brand-lockup">
      <span class="brand-square" aria-hidden="true"></span>
      <p class="brand-primary">TEMBROLIGHT OFFICE</p>
      <p class="brand-secondary">INTERIORS</p>
      <p class="services"><span>Office Furniture</span><span>Design</span><span>Installation</span></p>
    </div>
  </section>

</body>
</html>
```